Hargrove Orthopedics and Sports Medicine
Arthroscopy of the Knee and Shoulder
Hargrove Orthopedics and Sports Medicine -
Creative Brief
Cutting-Edge
Daniel K. Hargrove Jr., M.D.
418 North Pelham Street Corliss, OK 74819
quillmoth@mailvane.com
hargrovemd.com
under web address please add fb.com/hargrovemd Do not put email on the card
use large pic of logo or use another idea if you like

```html
<!DOCTYPE html>
<html lang="en">
<head>
<meta charset="utf-8">
<title>Hargrove Orthopedics and Sports Medicine – Business Card</title>
<link href="https://fonts.googleapis.com/css2?family=Source+Sans+3:wght@400;600;700&display=swap" rel="stylesheet">
<style>
  :root {
    --page-bg: #e9e6e2;
    --blue-deep: #1c3a86;
    --blue-mid: #2d5bb0;
    --blue-light: #5d8fd6;
    --card-white: #ffffff;
    --divider-grey: #8a8d93;
    --text-light: #ffffff;
    --brand-blue: #2a4f9e;
  }
  * { margin: 0; padding: 0; box-sizing: border-box; }
  html, body { width: 1200px; height: 852px; overflow: hidden; }
  body {
    background: var(--page-bg);
    font-family: "Source Sans 3", "Myriad Pro", Arial, sans-serif;
    display: flex; align-items: center; justify-content: center;
  }
  .business-card {
    position: relative;
    width: 1000px; height: 571px;
    border-radius: 34px;
    overflow: hidden;
    background: var(--card-white);
    box-shadow: 0 10px 30px rgba(0,0,0,0.18);
  }
  .card-shapes { position: absolute; inset: 0; }
  .contact-panel {
    position: absolute; left: 44px; top: 0; bottom: 0; width: 460px;
    color: var(--text-light);
  }
  .doctor-name { position: absolute; top: 46px; font-size: 31px; font-weight: 700; letter-spacing: 0.2px; white-space: nowrap; }
  .specialty { position: absolute; top: 86px; font-size: 22px; font-weight: 400; white-space: nowrap; }
  .address { position: absolute; top: 250px; font-size: 23px; line-height: 1.35; white-space: nowrap; }
  .contact-list { position: absolute; top: 338px; list-style: none; font-size: 22px; }
  .contact-list li { display: flex; align-items: center; gap: 14px; height: 34px; white-space: nowrap; }
  .contact-icon { width: 22px; height: 22px; flex: none; }
  .brand-block {
    position: absolute; left: 600px; top: 200px; width: 330px;
    display: flex; align-items: center; gap: 16px;
  }
  .brand-dot { width: 46px; height: 46px; border-radius: 50%; background: var(--brand-blue); flex: none; }
  .brand-name { font-size: 30px; font-weight: 700; line-height: 1.12; color: var(--brand-blue); }
</style>
</head>
<body>
  <div class="business-card">
    <svg class="card-shapes" viewBox="0 0 1000 571" width="1000" height="571" aria-hidden="true">
      <defs>
        <radialGradient id="panelGradient" cx="0.45" cy="0.55" r="0.7">
          <stop offset="0" stop-color="var(--blue-light)"/>
          <stop offset="0.55" stop-color="var(--blue-mid)"/>
          <stop offset="1" stop-color="var(--blue-deep)"/>
        </radialGradient>
      </defs>
      <path d="M0 0 H560 C 480 150, 470 400, 520 571 H0 Z" fill="url(#panelGradient)"/>
      <path d="M560 0 C 480 150, 470 400, 520 571 L540 571 C 490 400, 500 150, 585 0 Z" fill="var(--divider-grey)"/>
    </svg>

    <div class="contact-panel">
      <div class="doctor-name">Daniel K. Hargrove Jr., M.D.</div>
      <div class="specialty">Arthroscopy of the Knee and Shoulder</div>
      <div class="address">418 North Pelham Street<br>Corliss, OK 74819</div>
      <ul class="contact-list">
        <li>
          <svg class="contact-icon" viewBox="0 0 24 24"><path d="M6 3l4 4-2 3c1 2 4 5 6 6l3-2 4 4-3 3C10 21 3 14 3 6z" fill="#fff"/></svg>
          555 210 4800
        </li>
        <li>
          <svg class="contact-icon" viewBox="0 0 24 24"><rect x="5" y="2" width="14" height="20" rx="2" fill="#fff"/><rect x="8" y="6" width="8" height="5" fill="var(--blue-mid)"/></svg>
          555 210 4801
        </li>
        <li>
          <svg class="contact-icon" viewBox="0 0 24 24"><circle cx="12" cy="12" r="10" fill="none" stroke="#fff" stroke-width="2"/><path d="M2 12h20M12 2c4 4 4 16 0 20M12 2c-4 4-4 16 0 20" fill="none" stroke="#fff" stroke-width="1.5"/></svg>
          hargrovemd.com
        </li>
        <li>
          <svg class="contact-icon" viewBox="0 0 24 24"><circle cx="12" cy="12" r="10" fill="#fff"/></svg>
          fb.com/hargrovemd
        </li>
      </ul>
    </div>

    <div class="brand-block">
      <span class="brand-dot"></span>
      <span class="brand-name">Hargrove Orthopedics and Sports Medicine</span>
    </div>
  </div>
</body>
</html>
```